Business Card needed for Drainora, a growing Septic Service company

Drainora, a growing local septic service company in Pennsylvania, needs updated business cards. We'd like the business card to feature our logo and communicate that we provide Septic Pumping, Installations/Repairs, Restroom Rentals, and 24/7 Emergency Service. The business card should be eye-catching, bold, and clean/simple. We have been in business almost 10 years and would like to expand and update our business brand and image.

Target Market(s)

Residential and Commercial, New and Current Homeowners

Industry/Entity Type

Service

Contact Information for Business Card

Contact on the business card should be: Dale Pruitt Owner & Operator
Phone: 610-555-0187
Email: service@drainora.example
Website: www.drainora.example
Address: 812 Birchwell Lane Easton PA 18042

Font styles to use
Sans Serif

Colors

Designer to choose colors to be used in the design.

Requirements
Must have
• Feature logo on both side of business card.
Nice to have
• We envision the contact information on one side and our services listed on the other side. Utilize the green from the symbol in our logo as part of the design, overall design color scheme should be white, grey, black.

```html
<!DOCTYPE html>
<html lang="en">
<head>
<meta charset="utf-8">
<title>Drainora Business Card</title>
<link href="https://fonts.googleapis.com/css2?family=Montserrat:wght@400;500;700;800&display=swap" rel="stylesheet">
<style>
  :root {
    --bg: #454545;
    --card: #1f1f1f;
    --card-dark: #161616;
    --green: #6cc04a;
    --white: #ffffff;
    --grey-text: #d9d9d9;
  }
  * { margin: 0; padding: 0; box-sizing: border-box; }
  html, body { width: 1200px; height: 801px; overflow: hidden; }
  body {
    background: var(--bg);
    font-family: "Montserrat", sans-serif;
    position: relative;
  }
  .card {
    position: absolute;
    left: 320px;
    width: 560px;
    height: 320px;
    background: var(--card);
    border-bottom: 3px solid var(--green);
    overflow: hidden;
  }
  .card--front { top: 45px; }
  .card--back { top: 420px; }

  .wordmark {
    position: absolute;
    display: flex;
    align-items: center;
    gap: 12px;
    white-space: nowrap;
  }
  .wordmark__square {
    width: 44px; height: 44px;
    background: var(--green);
    flex: none;
  }
  .wordmark__name {
    color: var(--white);
    font-weight: 800;
    font-size: 46px;
    letter-spacing: 1px;
    line-height: 1;
  }
  .card--front .wordmark { left: 72px; top: 62px; }

  .person { position: absolute; left: 72px; top: 170px; }
  .person__name {
    color: var(--green);
    font-weight: 800;
    font-size: 21px;
    letter-spacing: 0.5px;
  }
  .person__title {
    color: var(--grey-text);
    font-size: 15px;
    margin-top: 4px;
  }
  .divider {
    position: absolute;
    left: 268px; top: 158px;
    width: 1px; height: 72px;
    background: var(--green);
  }
  .contacts { position: absolute; left: 288px; top: 160px; list-style: none; }
  .contacts li {
    display: flex; align-items: center; gap: 8px;
    color: var(--grey-text);
    font-size: 13.5px;
    margin-bottom: 6px;
  }
  .contacts svg { width: 13px; height: 13px; flex: none; }
  .address {
    position: absolute;
    left: 288px; top: 262px;
    color: var(--grey-text);
    font-size: 14px;
  }

  .pattern-field {
    position: absolute; inset: 0;
    background: linear-gradient(120deg, #0e0e0e 0%, #1c1c1c 55%, #2a2a2a 100%);
  }
  .logo-band {
    position: absolute;
    left: 160px; top: 175px;
    width: 400px; height: 72px;
    background: var(--card-dark);
  }
  .card--back .wordmark { left: 184px; top: 189px; }
</style>
</head>
<body>
  <section class="card card--front">
    <div class="wordmark">
      <span class="wordmark__square"></span>
      <span class="wordmark__name">DRAINORA</span>
    </div>
    <div class="person">
      <div class="person__name">DALE PRUITT</div>
      <div class="person__title">Owner &amp; Operator</div>
    </div>
    <span class="divider"></span>
    <ul class="contacts">
      <li>
        <svg viewBox="0 0 16 16"><path fill="#6cc04a" d="M3.5 1.5l2.5 0 1 3.5-1.6 1.2a8 8 0 0 0 4.4 4.4L11 9l3.5 1v2.5c0 1-1 2-2 2C6.5 14.5 1.5 9.5 1.5 3.5c0-1 1-2 2-2z"/></svg>
        610-555-0187
      </li>
      <li>
        <svg viewBox="0 0 16 16"><rect x="1" y="3" width="14" height="10" fill="#6cc04a"/><path d="M1 3l7 5.5L15 3" fill="none" stroke="#1f1f1f" stroke-width="1.4"/></svg>
        service@drainora.example
      </li>
      <li>
        <svg viewBox="0 0 16 16"><circle cx="8" cy="8" r="6.5" fill="none" stroke="#6cc04a" stroke-width="1.6"/><path d="M1.5 8h13M8 1.5c-3 3.5-3 9.5 0 13M8 1.5c3 3.5 3 9.5 0 13" fill="none" stroke="#6cc04a" stroke-width="1.2"/></svg>
        www.drainora.example
      </li>
    </ul>
    <div class="address">812 Birchwell Lane, Easton PA 18042</div>
  </section>

  <section class="card card--back">
    <div class="pattern-field" role="img" aria-label="Embossed tiled pattern of the brand symbol in dark grey tones"></div>
    <div class="logo-band"></div>
    <div class="wordmark">
      <span class="wordmark__square"></span>
      <span class="wordmark__name">DRAINORA</span>
    </div>
  </section>
</body>
</html>
```